Innovation Company Business Card Design

I need to have my business card updated. The current card was designed when the company started 2.5 years ago and was a quick and dirty job.

I need a new card design that is more professional and has my updated company tag line.

I will include the old card's Corel Draw file, and EPS versions as examples of the current design. I will also include the company logo eps and corel version files.

The company pantone colour is pantone 1805 c (a dark red)

I want the design to convey the nature of our business as a strategic technology innovation company, but yet still be professional. We are funky vibey and work from an industrial style office in a vibey designer dominat part of town. Though are clients include large banks and corporate clients too.

The information that needs to be on the card is in attached word document (but doesn't have to be in this order or format)

Final version needs to be supplied in PNG preview, as well as PSD file format (or other editable file version) so that personal information on card can be easily edited and reprinted.

Target Market(s)

CEO's of small to medium size companies
Marketing Managers of large coporates
Account managers of Digital Agencies

Industry/Entity Type

Business

Requirements
Must have
• 86x54mm will be cut in rounded corner credit card size format (Except if you recommend otherwise in your design)
Nice to have
• Some kind of background transparency combined with the pantone colour that gives the card some dimension and depth. But no gradient fills please :-)
Should not have
• Basic gradient fills
• Clipart

```html
<!DOCTYPE html>
<html lang="en">
<head>
<meta charset="utf-8">
<title>Vantora Business Card</title>
<link href="https://fonts.googleapis.com/css2?family=Arimo:wght@400;700&display=swap" rel="stylesheet">
<style>
  :root {
    --brand-red: #a91f2e;
    --paper: #ffffff;
    --ink: #1d1d1d;
    --backdrop: #e9e6e1;
  }
  * { margin: 0; padding: 0; box-sizing: border-box; }
  html, body { width: 1200px; height: 1023px; overflow: hidden; }
  body {
    background: var(--backdrop);
    font-family: "Arimo", Arial, sans-serif;
    display: flex;
    align-items: center;
    justify-content: center;
    gap: 60px;
  }
  .card {
    width: 516px;
    height: 324px;
    border-radius: 30px;
    position: relative;
    box-shadow: 0 6px 18px rgba(0,0,0,0.18);
  }
  .card-front { background: var(--paper); color: var(--ink); }
  .card-back { background: var(--brand-red); color: var(--paper); }

  .contact {
    position: absolute;
    left: 262px;
    top: 40px;
    font-size: 14px;
    line-height: 1.45;
  }
  .contact-name { color: var(--brand-red); font-weight: 700; font-size: 21px; line-height: 1.2; }
  .contact-role { font-size: 15px; margin-bottom: 6px; }
  .contact-company { color: var(--brand-red); margin-top: 12px; }
  .label { color: var(--brand-red); }

  .front-brand {
    position: absolute;
    left: 40px;
    bottom: 44px;
    display: flex;
    align-items: center;
    gap: 12px;
  }
  .brand-square { width: 26px; height: 26px; background: var(--brand-red); }
  .front-brand .brand-name {
    color: var(--brand-red);
    font-weight: 700;
    font-size: 40px;
  }

  .back-brand {
    position: absolute;
    left: 64px;
    top: 96px;
  }
  .back-brand .brand-name {
    font-weight: 700;
    font-size: 60px;
    line-height: 1;
    letter-spacing: -1px;
  }
  .tagline {
    font-size: 14px;
    margin-top: 6px;
    margin-left: 44px;
  }
  .website {
    position: absolute;
    right: 52px;
    bottom: 42px;
    font-weight: 700;
    font-size: 14px;
  }
</style>
</head>
<body>
  <section class="card card-front">
    <div class="contact">
      <p class="contact-name">Daniel Marsh</p>
      <p class="contact-role">Founder &amp; MD</p>
      <p><span class="label">E.</span> daniel@vantora.com</p>
      <p><span class="label">M.</span> 0824417302</p>
      <p class="contact-company">Vantora (Pty) Ltd</p>
      <p>Suite 210, 14 Milner Rd.</p>
      <p>Parkview, JHB, RSA</p>
      <p><span class="label">P.</span> 010 482 3365</p>
    </div>
    <div class="front-brand">
      <span class="brand-square"></span>
      <span class="brand-name">Vantora</span>
    </div>
  </section>

  <section class="card card-back">
    <div class="back-brand">
      <p class="brand-name">Vantora</p>
      <p class="tagline">Strategic Innovation</p>
    </div>
    <p class="website">www.vantora.com</p>
  </section>
</body>
</html>
```